2 sided postcard for New Internet Customers

We would like a design for a two sided postcard (with room for mailing label), dimensions 9 1/4 by 6 1/4 to be sent via US Mail.

The postcard needs to include our logo (attached) and the text
Fiber Optic Internet
555-219-8063
http://www.brightwirenet.example
Speeds up to 1 Gig, with packages starting at $55

These will be sent to people who do not have our service.

Since this is going to be "junk mail" we probably only have 1 second or less to capture someone's attention to encourage them to read the entire postcard.

We are a "mom and pop" telecommunications company that provides internet, phone, and television services on the fiber optic network that we designed, built, and maintain.

We started as a dial up ISP in 1995, and have extraordinary technical support based in Freeport PA, our customers actually get the speeds they pay for, and our service is highly reliable.

We have a slogan (which you can choose to use or ignore) which is
"I Went Fast with Kornwell"

Existing customers can earn a $50 credit for every new customer they refer to us. Unlike most large cable and internet companies we have very happy customers... some who have stayed with us for decades.

I've attached our previous postcard, which I really dislike. It does have a blank spot for where the mailing label should go.

Target Market(s)

New Internet Customers in Western Pennsylvania

Industry/Entity Type

Internet

Font styles to use
Other font styles liked:
• Just match our logo.

Colors

Designer to choose colors to be used in the design.

Requirements
Must have
• The postcard needs to include our logo, and the text Fiber Optic Internet 555-219-8063 http://www.brightwirenet.example Speeds up to 1 Gig, with packages starting at $55
Nice to have
• The colors and fonts should look good with our logo.
Should not have
• Should not have small print or lots of text. Both sides need to capture attention.

```html
<!DOCTYPE html>
<html lang="en">
<head>
<meta charset="utf-8">
<title>Kornwell Fiber Optic Internet Postcard</title>
<link rel="stylesheet" href="https://fonts.googleapis.com/css2?family=Barlow+Condensed:ital,wght@1,700;1,800&family=Montserrat:wght@400;700&display=swap">
<style>
  :root {
    --page: #e4e7eb;
    --navy: #0a121d;
    --navy-soft: #17212e;
    --blue: #1f72c2;
    --red: #ee1c25;
    --white: #ffffff;
    --ink: #0d0d0d;
    --silver: #8b8f96;
    --cyan: #2fb8e6;
    --deep-blue: #0d2f4f;
  }
  * { box-sizing: border-box; margin: 0; padding: 0; }
  html, body { width: 1200px; height: 1114px; overflow: hidden; }
  body { background: var(--page); position: relative; font-family: "Montserrat", sans-serif; }

  .card { position: absolute; left: 282px; width: 636px; height: 429px; overflow: hidden; background: var(--navy); }
  .card--front { top: 122px; }
  .card--back { top: 563px; background: var(--white); }

  .hero-art {
    position: absolute; left: 290px; top: 0; width: 346px; height: 429px;
    background:
      radial-gradient(ellipse at 45% 45%, rgba(47,184,230,.75) 0%, rgba(13,47,79,.7) 45%, rgba(10,18,29,0) 75%),
      linear-gradient(90deg, var(--navy) 0%, var(--deep-blue) 35%, #16436a 70%, #0e2236 100%);
  }

  .brand { position: absolute; display: flex; align-items: center; }
  .brand__dot { border-radius: 50%; background: var(--blue); flex: none; }
  .brand__name { font-family: "Montserrat", sans-serif; font-weight: 400; color: var(--white); white-space: nowrap; }
  .brand__slogan { position: absolute; font-family: "Montserrat", sans-serif; font-weight: 400; color: var(--white); white-space: nowrap; text-align: right; }

  .headline-band {
    position: absolute; display: flex; align-items: center;
    border-top: 1px solid rgba(255,255,255,.35); border-bottom: 1px solid rgba(255,255,255,.35);
    font-family: "Barlow Condensed", sans-serif; font-style: italic; font-weight: 800; color: var(--white); white-space: nowrap;
  }
  .headline-band .accent { color: var(--red); }

  .speeds { position: absolute; font-family: "Barlow Condensed", sans-serif; font-style: italic; font-weight: 700; color: var(--white); line-height: 1.3; }

  .price-band { position: absolute; display: flex; align-items: center; }
  .price { font-family: "Barlow Condensed", sans-serif; font-style: italic; font-weight: 800; color: var(--red); line-height: 1; text-shadow: 2px 3px 3px rgba(0,0,0,.35); }

  .phone-pill { position: absolute; display: flex; align-items: center; background: var(--white); border-radius: 26px 0 26px 0; overflow: hidden; }
  .phone-pill__icon { height: 100%; width: 92px; background: var(--blue); display: flex; align-items: center; justify-content: center; border-radius: 26px 0 0 0; }
  .phone-pill__number { font-family: "Barlow Condensed", sans-serif; font-style: italic; font-weight: 800; color: var(--ink); font-size: 27px; padding-left: 12px; white-space: nowrap; }

  .web { font-family: "Montserrat", sans-serif; font-weight: 700; white-space: nowrap; }

  /* front specifics */
  .card--front .brand { left: 34px; top: 15px; }
  .card--front .brand__dot { width: 94px; height: 94px; }
  .card--front .brand__name { font-size: 34px; margin-left: 23px; margin-top: -12px; }
  .card--front .brand__slogan { left: 190px; top: 86px; width: 181px; font-size: 11px; }
  .card--front .headline-band { left: 0; top: 124px; width: 400px; height: 42px; padding-left: 18px; font-size: 32px;
    background: linear-gradient(90deg, rgba(10,18,29,.95) 0%, rgba(10,18,29,.75) 75%, rgba(10,18,29,.2) 100%); }
  .card--front .speeds { left: 17px; top: 176px; font-size: 24px; }
  .card--front .price-band { left: 0; top: 247px; width: 315px; height: 98px; padding-left: 16px;
    background: linear-gradient(90deg, var(--white) 0%, var(--white) 55%, var(--silver) 85%, rgba(139,143,150,0) 100%); }
  .card--front .price { font-size: 92px; }
  .card--front .phone-pill { left: 15px; top: 361px; width: 268px; height: 51px; }
  .card--front .web-band { position: absolute; left: 315px; top: 368px; width: 321px; height: 38px; background: var(--white);
    display: flex; align-items: center; justify-content: center; }
  .card--front .web { font-size: 16px; color: var(--ink); }

  /* back specifics */
  .back-panel { position: absolute; left: 0; top: 0; width: 315px; height: 429px; background: var(--navy); }
  .card--back .brand { left: 34px; top: 18px; }
  .card--back .brand__dot { width: 68px; height: 68px; }
  .card--back .brand__name { font-size: 27px; margin-left: 20px; margin-top: -8px; }
  .card--back .brand__slogan { left: 140px; top: 70px; width: 140px; font-size: 9px; }
  .card--back .headline-band { left: 13px; top: 101px; width: 290px; height: 46px; justify-content: center; font-size: 28px; }
  .card--back .speeds { left: 0; top: 153px; width: 315px; text-align: center; font-size: 22px; }
  .card--back .price-band { left: 13px; top: 221px; width: 284px; height: 98px; justify-content: center;
    background: linear-gradient(90deg, #3a3f47 0%, var(--white) 35%, var(--white) 65%, #3a3f47 100%); }
  .card--back .price { font-size: 90px; }
  .card--back .phone-pill { left: 24px; top: 330px; width: 266px; height: 52px; }
  .card--back .web { position: absolute; left: 0; top: 393px; width: 315px; text-align: center; font-size: 17px; color: var(--white); }

  .stamp-box { position: absolute; left: 497px; top: 25px; width: 95px; height: 124px; border: 1px solid var(--ink); }
  .address-line { position: absolute; left: 359px; width: 233px; height: 0; border-top: 1px solid var(--ink); }
</style>
</head>
<body>

<section class="card card--front" aria-label="Postcard front">
  <div class="hero-art" role="img" aria-label="Illustration of a hooded gamer with headphones holding a controller, surrounded by glowing blue lightning"></div>

  <div class="brand">
    <span class="brand__dot"></span>
    <span class="brand__name">Kornwell, Inc.</span>
  </div>
  <p class="brand__slogan">I Went Fast with Kornwell</p>

  <h1 class="headline-band">FIBER OPTIC /&nbsp;<span class="accent">INTERNET</span></h1>
  <p class="speeds">Speeds up to 1 Gig,<br>with packages starting at</p>
  <div class="price-band"><span class="price">$55</span></div>

  <div class="phone-pill">
    <span class="phone-pill__icon">
      <svg width="34" height="34" viewBox="0 0 24 24" aria-hidden="true">
        <path d="M6.6 10.8a15 15 0 0 0 6.6 6.6l2.2-2.2a1 1 0 0 1 1-.25 11.4 11.4 0 0 0 3.6.57 1 1 0 0 1 1 1V20a1 1 0 0 1-1 1A17 17 0 0 1 3 4a1 1 0 0 1 1-1h3.5a1 1 0 0 1 1 1c0 1.25.2 2.45.57 3.57a1 1 0 0 1-.25 1z" fill="#fff"/>
        <path d="M14 3.5a6.5 6.5 0 0 1 6.5 6.5M14 6.5a3.5 3.5 0 0 1 3.5 3.5" stroke="#fff" stroke-width="1.6" fill="none" stroke-linecap="round"/>
      </svg>
    </span>
    <span class="phone-pill__number">555-219-8063</span>
  </div>

  <div class="web-band"><span class="web">www.brightwirenet.example</span></div>
</section>

<section class="card card--back" aria-label="Postcard back">
  <div class="back-panel">
    <div class="brand">
      <span class="brand__dot"></span>
      <span class="brand__name">Kornwell, Inc.</span>
    </div>
    <p class="brand__slogan">I Went Fast with Kornwell</p>

    <h2 class="headline-band">FIBER OPTIC /&nbsp;<span class="accent">INTERNET</span></h2>
    <p class="speeds">Speeds up to 1 Gig,<br>with packages starting at</p>
    <div class="price-band"><span class="price">$55</span></div>

    <div class="phone-pill">
      <span class="phone-pill__icon">
        <svg width="34" height="34" viewBox="0 0 24 24" aria-hidden="true">
          <path d="M6.6 10.8a15 15 0 0 0 6.6 6.6l2.2-2.2a1 1 0 0 1 1-.25 11.4 11.4 0 0 0 3.6.57 1 1 0 0 1 1 1V20a1 1 0 0 1-1 1A17 17 0 0 1 3 4a1 1 0 0 1 1-1h3.5a1 1 0 0 1 1 1c0 1.25.2 2.45.57 3.57a1 1 0 0 1-.25 1z" fill="#fff"/>
          <path d="M14 3.5a6.5 6.5 0 0 1 6.5 6.5M14 6.5a3.5 3.5 0 0 1 3.5 3.5" stroke="#fff" stroke-width="1.6" fill="none" stroke-linecap="round"/>
        </svg>
      </span>
      <span class="phone-pill__number">555-219-8063</span>
    </div>

    <p class="web">www.brightwirenet.example</p>
  </div>

  <div class="stamp-box" aria-label="Stamp area"></div>
  <div class="address-line" style="top:291px"></div>
  <div class="address-line" style="top:318px"></div>
  <div class="address-line" style="top:344px"></div>
  <div class="address-line" style="top:370px"></div>
</section>

</body>
</html>
```